varnoth company need business card, envelope and letterhead design

Check on the attached file wherein you can find our logo and information about the company
Business card will double sided English version and Arabic version

Industry/Entity Type

Business

Requirements
Must have
• include the design also for the letterhead and envelop
Nice to have

```html
<!DOCTYPE html>
<html lang="en">
<head>
<meta charset="utf-8">
<title>Varnoth Stationery</title>
<link rel="stylesheet" href="https://fonts.googleapis.com/css2?family=Open+Sans:ital,wght@0,400;0,600;0,700;1,400&display=swap">
<style>
  :root {
    --brand-blue: #1f6fc1;
    --ink: #3a3f45;
    --muted: #6b7178;
    --paper: #ffffff;
    --backdrop: #e6e9ea;
    --edge: #d3d7d9;
  }
  * { box-sizing: border-box; margin: 0; padding: 0; }
  html, body { width: 1200px; height: 900px; overflow: hidden; }
  body {
    background: var(--backdrop);
    font-family: "Open Sans", sans-serif;
    color: var(--ink);
    position: relative;
  }
  .sheet {
    position: absolute;
    background: var(--paper);
    border: 1px solid var(--edge);
    box-shadow: 0 2px 6px rgba(0,0,0,0.08);
    overflow: hidden;
  }
  .wordmark {
    display: flex;
    align-items: center;
    gap: 8px;
    color: var(--brand-blue);
    font-weight: 700;
    letter-spacing: 0.06em;
    text-transform: uppercase;
  }
  .wordmark__dot {
    background: var(--brand-blue);
    display: block;
  }
  .footer-band {
    position: absolute;
    left: 0; right: 0; bottom: 0;
    background: var(--brand-blue);
    color: #fff;
    display: flex;
    align-items: center;
    justify-content: center;
    font-weight: 600;
  }

  /* Letterhead */
  .letterhead { left: 610px; top: 54px; width: 550px; height: 778px; }
  .letterhead .wordmark { position: absolute; left: 40px; top: 42px; font-size: 26px; }
  .letterhead .wordmark__dot { width: 22px; height: 22px; }
  .contact-block {
    position: absolute;
    right: 40px; top: 44px;
    border-left: 2px solid var(--brand-blue);
    padding-left: 8px;
    font-size: 9px;
    line-height: 1.45;
    color: var(--muted);
  }
  .letterhead .footer-band { height: 26px; font-size: 10px; bottom: 26px; }

  /* Envelope */
  .envelope { left: 40px; top: 520px; width: 520px; height: 260px; }
  .envelope .wordmark { position: absolute; left: 28px; top: 26px; font-size: 24px; }
  .envelope .wordmark__dot { width: 20px; height: 20px; }
  .envelope__sender {
    position: absolute; left: 28px; top: 66px;
    font-size: 9.5px; line-height: 1.5; color: var(--muted);
  }
  .envelope .footer-band { height: 22px; font-size: 9.5px; bottom: 18px; }

  /* Business cards */
  .card { width: 330px; height: 190px; left: 40px; }
  .card--front { top: 70px; }
  .card--back { top: 290px; }
  .card .wordmark { position: absolute; right: 22px; top: 30px; font-size: 18px; gap: 6px; }
  .card .wordmark__dot { width: 14px; height: 14px; }
  .card__person { position: absolute; left: 22px; top: 24px; }
  .card__name { font-size: 11px; font-weight: 700; color: var(--ink); }
  .card__role { font-size: 9px; font-style: italic; color: var(--brand-blue); }
  .card__contacts {
    position: absolute; left: 22px; top: 70px;
    list-style: none; font-size: 8.5px; line-height: 1.75; color: var(--muted);
  }
  .card__contacts li { display: flex; align-items: center; gap: 6px; }
  .card__contacts li::before {
    content: ""; width: 5px; height: 5px; border-radius: 50%;
    background: var(--brand-blue); display: block;
  }
  .card__rule {
    position: absolute; left: 22px; right: 22px; top: 150px;
    border-top: 1px solid var(--edge);
  }
  .card__address {
    position: absolute; left: 22px; right: 22px; top: 158px;
    font-size: 7.5px; color: var(--muted); text-align: right;
  }
</style>
</head>
<body>

  <section class="sheet card card--front" aria-label="Business card">
    <div class="card__person">
      <p class="card__name">Fahad Bin Omar Al Rashed</p>
      <p class="card__role">General Manager</p>
    </div>
    <div class="wordmark"><span class="wordmark__dot"></span>Varnoth</div>
    <ul class="card__contacts">
      <li>011 4820 337</li>
      <li>011 4820 338</li>
      <li>+966 551 204 778</li>
      <li>hello.varnoth@mail.com</li>
    </ul>
    <div class="card__rule"></div>
    <p class="card__address">Qasr Al Noor Street- Al Wadi- P.O. Box 4120-11365</p>
  </section>

  <section class="sheet card card--back" aria-label="Business card, second side">
    <div class="card__person">
      <p class="card__name">Fahad Bin Omar Al Rashed</p>
      <p class="card__role">General Manager</p>
    </div>
    <div class="wordmark"><span class="wordmark__dot"></span>Varnoth</div>
    <ul class="card__contacts">
      <li>011 4820 337</li>
      <li>011 4820 338</li>
      <li>+966 551 204 778</li>
      <li>www.varnoth.com</li>
    </ul>
    <div class="card__rule"></div>
    <p class="card__address">Qasr Al Noor Street- Al Wadi- P.O. Box 4120-11365</p>
  </section>

  <section class="sheet envelope" aria-label="Envelope">
    <div class="wordmark"><span class="wordmark__dot"></span>Varnoth</div>
    <p class="envelope__sender">
      Qasr Al Noor Street- Al Wadi- P.O. Box 4120-11365<br>
      Kingdom of Saudi Arabia
    </p>
    <div class="footer-band">Qasr Al Noor Street- Al Wadi- P.O. Box 4120-11365, Kingdom of Saudi Arabia</div>
  </section>

  <section class="sheet letterhead" aria-label="Letterhead">
    <div class="wordmark"><span class="wordmark__dot"></span>Varnoth</div>
    <address class="contact-block" style="font-style: normal;">
      Qasr Al Noor Street- Al Wadi<br>
      P.O. Box 4120-11365<br>
      Kingdom of Saudi Arabia<br>
      Tel: 011 4820 337 - Fax: 011 4820 338<br>
      hello.varnoth@mail.com
    </address>
    <div class="footer-band">Qasr Al Noor Street- Al Wadi- P.O. Box 4120-11365, Kingdom of Saudi Arabia</div>
  </section>

</body>
</html>
```